Company service wheel graphic

A graphic demonstrating all the services the company offers.
I have hand drawn and written up on the attached the content that is required. Also attached is our company logo so you have a sense of the colour scheme of the logo.
This will eventually go into a company brochure, be used on our website etc.

Target Market(s)

Local GOvernment and other professionals who work in the sport, recreation and leisure industries

Industry/Entity Type

Sports, recreation, leisure, aquatics

Font styles to use
Other font styles liked:
• Calibri

Colors
0054AA
0677BA
7BADD7
CADEEF
E8F1F8

Requirements
Must have
• An eye catching graphic that captures all the information in the hand drawn atachement.
Nice to have
• Each quadrant in the circle to have its own colour, that links to the company logo

```html
<!DOCTYPE html>
<html lang="en">
<head>
<meta charset="utf-8">
<title>Service Wheel</title>
<link rel="stylesheet" href="https://fonts.googleapis.com/css2?family=Source+Sans+3:wght@400;600;700&display=swap">
<style>
  :root {
    --blue-mid: #0A86C6;
    --blue-deep: #0057A5;
    --blue-bright: #00A7E4;
    --navy: #0C2A5E;
    --white: #FFFFFF;
    --paper: #FFFFFF;
  }
  html, body {
    margin: 0;
    padding: 0;
    width: 1200px;
    height: 1200px;
    overflow: hidden;
    background: var(--paper);
  }
  .service-wheel {
    display: block;
    width: 1200px;
    height: 1200px;
    font-family: "Source Sans 3", "Calibri", sans-serif;
  }
  .quadrant--mid { fill: var(--blue-mid); }
  .quadrant--deep { fill: var(--blue-deep); }
  .bar { fill: var(--navy); }
  .hub { fill: var(--blue-bright); }
  .audience {
    fill: var(--navy);
    font-size: 27px;
    font-weight: 400;
    letter-spacing: 1px;
    text-transform: uppercase;
  }
  .service {
    fill: var(--white);
    font-size: 21px;
    font-weight: 400;
  }
  .bullet { fill: var(--white); }
  .bar-label, .cell-label {
    fill: var(--white);
    font-size: 20px;
    text-anchor: middle;
  }
  .cell-label--small { font-size: 18px; }
  .hub-label {
    fill: var(--white);
    font-size: 21px;
    font-weight: 700;
    text-anchor: middle;
  }
</style>
</head>
<body>
<svg class="service-wheel" viewBox="0 0 1040 1040" xmlns="http://www.w3.org/2000/svg" role="img" aria-label="Service wheel: community and stakeholder engagement at the centre of planning, management, participation and community outcomes">
  <defs>
    <polygon id="bullet-mark" class="bullet" points="0,-7 12,0 0,7"/>
    <path id="arc-government" d="M94.1 321.2 A470 470 0 0 1 503.6 50.3"/>
    <path id="arc-managers" d="M536.4 50.3 A470 470 0 0 1 967.0 374.8"/>
    <path id="arc-investors" d="M28.2 554.4 A493 493 0 0 0 563 1011.1"/>
    <path id="arc-providers" d="M571.5 1010.3 A493 493 0 0 0 1012.3 545.8"/>
  </defs>

  <!-- Quadrants -->
  <g class="quadrants">
    <path class="quadrant--mid" d="M520 520 L62 520 A458 458 0 0 1 520 62 Z"/>
    <path class="quadrant--deep" d="M520 520 L520 62 A458 458 0 0 1 978 520 Z"/>
    <path class="quadrant--mid" d="M520 520 L978 520 A458 458 0 0 1 520 978 Z"/>
    <path class="quadrant--deep" d="M520 520 L520 978 A458 458 0 0 1 62 520 Z"/>
  </g>

  <!-- Audience labels around the ring -->
  <g class="audiences">
    <text class="audience"><textPath href="#arc-government" startOffset="50%" text-anchor="middle">Local + State Government</textPath></text>
    <text class="audience"><textPath href="#arc-managers" startOffset="50%" text-anchor="middle">Sport + Leisure Facility Managers</textPath></text>
    <text class="audience"><textPath href="#arc-investors" startOffset="50%" text-anchor="middle">Investors, Developers, Architects + Designers</textPath></text>
    <text class="audience"><textPath href="#arc-providers" startOffset="50%" text-anchor="middle">Sport, Recreation + Community Providers</textPath></text>
  </g>

  <!-- Planning services -->
  <g class="services services--planning">
    <use href="#bullet-mark" x="283" y="169"/>
    <text class="service" x="310" y="176">Feasibility Studies</text>
    <use href="#bullet-mark" x="222" y="208"/>
    <text class="service" x="248" y="215">Community +</text>
    <text class="service" x="248" y="245">Stakeholder Research</text>
    <use href="#bullet-mark" x="166" y="282"/>
    <text class="service" x="193" y="289">Sport + Recreation Strategies</text>
    <use href="#bullet-mark" x="131" y="330"/>
    <text class="service" x="157" y="337">Design Strategies</text>
    <use href="#bullet-mark" x="112" y="378"/>
    <text class="service" x="138" y="385">Indoor +</text>
    <text class="service" x="138" y="415">Outdoor Spaces</text>
  </g>

  <!-- Management services -->
  <g class="services services--management">
    <use href="#bullet-mark" x="536" y="133"/>
    <text class="service" x="562" y="140">Activating</text>
    <text class="service" x="562" y="170">Underutilised Assets</text>
    <use href="#bullet-mark" x="536" y="201"/>
    <text class="service" x="564" y="208">Income + Revenue</text>
    <text class="service" x="564" y="238">Generation Strategies</text>
    <use href="#bullet-mark" x="536" y="272"/>
    <text class="service" x="568" y="279">Mystery Shopper + Business</text>
    <text class="service" x="568" y="309">Health Checks</text>
    <use href="#bullet-mark" x="713" y="344"/>
    <text class="service" x="741" y="351">Financial +</text>
    <text class="service" x="741" y="381">Funding strategies</text>
    <use href="#bullet-mark" x="713" y="413"/>
    <text class="service" x="741" y="420">Management</text>
    <text class="service" x="741" y="450">Support</text>
    <use href="#bullet-mark" x="713" y="484"/>
    <text class="service" x="743" y="491">Business Planning</text>
  </g>

  <!-- Participation services -->
  <g class="services services--participation">
    <use href="#bullet-mark" x="88" y="556"/>
    <text class="service" x="116" y="563">Trends + Insights</text>
    <use href="#bullet-mark" x="100" y="599"/>
    <text class="service" x="128" y="606">Health Profiling</text>
    <use href="#bullet-mark" x="114" y="640"/>
    <text class="service" x="142" y="647">Active Recreation</text>
    <text class="service" x="142" y="677">Strategies</text>
    <use href="#bullet-mark" x="140" y="709"/>
    <text class="service" x="168" y="716">Community</text>
    <text class="service" x="168" y="746">Program Development</text>
    <use href="#bullet-mark" x="189" y="783"/>
    <text class="service" x="217" y="790">Physical Activity Strategies</text>
    <use href="#bullet-mark" x="214" y="823"/>
    <text class="service" x="240" y="830">Specific Cohort Strategies</text>
    <use href="#bullet-mark" x="260" y="866"/>
    <text class="service" x="287" y="873">Sports + Program</text>
    <text class="service" x="307" y="903">Specific Strategies</text>
  </g>

  <!-- Outcome services -->
  <g class="services services--outcomes">
    <use href="#bullet-mark" x="714" y="575"/>
    <text class="service" x="742" y="582">Community Impact</text>
    <text class="service" x="742" y="612">Monitoring</text>
    <use href="#bullet-mark" x="714" y="656"/>
    <text class="service" x="741" y="663">Social Value</text>
    <use href="#bullet-mark" x="558" y="749"/>
    <text class="service" x="586" y="756">Community Outcomes +</text>
    <text class="service" x="586" y="786">KPIs</text>
    <use href="#bullet-mark" x="556" y="825"/>
    <text class="service" x="583" y="832">Contract Monitoring</text>
  </g>

  <!-- Core matrix -->
  <g class="core">
    <rect class="quadrant--deep" x="347" y="390" width="173" height="130"/>
    <rect class="quadrant--mid" x="520" y="390" width="174" height="130"/>
    <rect class="quadrant--mid" x="347" y="520" width="173" height="135"/>
    <rect class="quadrant--deep" x="520" y="520" width="174" height="135"/>

    <rect class="bar" x="347" y="323" width="347" height="67"/>
    <text class="bar-label" x="520" y="348">Community, Aquatic +</text>
    <text class="bar-label" x="520" y="375">Recreation Facilities</text>

    <rect class="bar" x="347" y="655" width="347" height="63"/>
    <text class="bar-label" x="520" y="692">Community Activation</text>

    <text class="cell-label" x="427" y="417">Planning</text>
    <text class="cell-label" x="605" y="417">Management</text>
    <text class="cell-label" x="422" y="620">Growing</text>
    <text class="cell-label" x="432" y="645">Participation</text>
    <text class="cell-label cell-label--small" x="634" y="619">Community</text>
    <text class="cell-label cell-label--small" x="624" y="643">Impact + Outcomes</text>

    <circle class="hub" cx="520" cy="518" r="97"/>
    <text class="hub-label" x="520" y="477">Community</text>
    <text class="hub-label" x="520" y="506">+</text>
    <text class="hub-label" x="520" y="537">Stakeholder</text>
    <text class="hub-label" x="520" y="567">Engagement</text>
  </g>
</svg>
</body>
</html>
```